Vitamin and Nutrition Ecommerce Site Needs a High End Website Design

We need a new and improved Homepage design for a leading Vitamin eCommerce business.
We supply our customers worldwide with leading brands of vitamin supplements and nutritional products at discounted prices.
The site design and layout must improve sales conversion and maximize the user experience staying on the site!

We will need to see;
A New Pillbox Lounge stylized font (no logo)
High-End Modern Design
Easy Sales Conversion Experience
Excellent Layout, Fast Navigation
Quality Font style, Stylish Colour Palette Selection
Appropriate Spacing
Call To Action to Improve Sales Conversion
Web page should Look Clean and Minimalist

The design should improve sales, communicate easy to find products, facilitate fast ordering, have a modern and professional appearance centered toward a predominately female consumer.

Thank you for your interest in this project!

Current design can be found on this link;
www.pillboxlounge.com.au/pillb/

Target Market(s)

80% Female 30-65 years

Industry/Entity Type

Business

Number of Pages Required

1 page

Colors

Designer to choose colors to be used in the design.

Requirements
Must have
• design must result improve sales conversion
• new Pillbox Lounge font design
• search field
• attractive clean modern design
• stylish font and colour palette selection
Nice to have
• white background
Should not have
• cluttered or busy layout
• confusing navigation

```html
<!DOCTYPE html>
<html lang="en">
<head>
<meta charset="utf-8">
<title>Pillbox Lounge – Home</title>
<link href="https://fonts.googleapis.com/css2?family=Open+Sans:wght@300;400;600;700&display=swap" rel="stylesheet">
<style>
:root{
  --mint:#93dcb9;
  --mint-deep:#5cc194;
  --brown:#5b4741;
  --brown-dark:#4a3a35;
  --ink:#333333;
  --muted:#666666;
  --line:#e3e3e3;
  --card:#f0f0f0;
  --white:#ffffff;
}
*{box-sizing:border-box;margin:0;padding:0}
html,body{width:1200px;height:3082px;overflow:hidden}
body{font-family:'Open Sans',Arial,sans-serif;color:var(--ink);background:var(--white);position:relative}
a{color:inherit;text-decoration:none}
.abs{position:absolute}

/* top bar */
.topbar{top:0;left:0;width:1200px;height:35px;border-bottom:1px solid var(--line);font-size:11px}
.topbar .promo{left:110px;top:10px;font-weight:700}
.topbar .account{right:110px;top:10px;display:flex;gap:8px;color:var(--muted)}
.topbar .account span.sep{color:#bbb}

/* header */
.header{top:35px;left:0;width:1200px;height:113px}
.wordmark{font-weight:400;color:var(--ink);letter-spacing:-.5px;display:flex;align-items:center;gap:10px}
.wordmark i{display:block;border-radius:50%;background:var(--mint-deep)}
.header .wordmark{left:100px;top:34px;font-size:38px}
.header .wordmark i{width:16px;height:16px}
.search{left:760px;top:42px;width:315px;height:36px;border-bottom:1px solid var(--line);font-size:11px;color:#999;display:flex;align-items:center;justify-content:space-between;padding:0 6px}

/* nav */
.nav{top:148px;left:0;width:1200px;height:60px;background:var(--mint);display:flex;justify-content:center;align-items:center;gap:22px;font-size:13px;color:#2f3b35}
.nav .current{font-weight:700}

/* hero */
.hero{top:208px;left:0;width:1200px;height:425px;background:linear-gradient(90deg,#f2f2f2,#ffffff)}
.hero-photo{left:0;top:0;width:582px;height:425px;background:linear-gradient(135deg,#d9cfc8,#b9a89c 55%,#e8e2dc)}
.hero .wordmark{left:725px;top:70px;font-size:40px}
.hero .wordmark i{width:18px;height:18px}
.hero-products{left:740px;top:160px;width:460px;height:265px;background:linear-gradient(180deg,#e6ede6,#9fcf8a 60%,#e9dd6a)}
.dots{left:135px;top:390px;display:flex;gap:10px}
.dots span{width:7px;height:7px;border-radius:50%;background:#fff}

/* usp strip */
.usps{top:633px;left:0;width:1200px;height:90px;border-bottom:1px solid var(--line);display:flex;justify-content:center;gap:62px;align-items:center}
.usp{display:flex;gap:12px;align-items:center}
.usp b{display:block;font-size:19px;font-weight:700;line-height:1.05}
.usp small{display:block;font-size:11px;color:var(--muted);font-weight:600}

/* welcome */
.welcome{top:770px;left:0;width:1200px;text-align:center}
.section-title{font-size:22px;font-weight:400}
.section-title strong{font-weight:700}
.rule{width:50px;height:2px;background:var(--mint);margin:8px auto 0}
.welcome p{width:840px;margin:16px auto 0;font-size:13px;line-height:22px;color:#444}
.btn-outline{display:inline-block;margin-top:22px;width:110px;height:40px;line-height:38px;border:1px solid #ccc;font-size:14px;font-weight:700}

/* tabs */
.tabs{top:972px;left:0;width:1200px;display:flex;justify-content:center;gap:26px;font-size:19px;color:#555}
.tabs .active{font-weight:700;color:var(--ink);border-bottom:2px solid var(--ink);padding-bottom:6px}
.tabs .sep{color:#888}

/* products */
.product{top:1048px;width:205px;height:345px;border:1px solid var(--line)}
.product .thumb{height:252px;margin:0;background:linear-gradient(180deg,#fff,#f3f3f3);display:flex;align-items:center;justify-content:center}
.product .thumb div{width:90px;height:170px;border-radius:8px}
.product h3{font-size:11px;font-weight:400;text-align:center;padding:12px 8px 0;height:56px;line-height:14px;border-top:1px solid var(--line)}
.product .buy{display:flex;align-items:center;padding:0 8px;gap:8px;font-size:15px}
.product .buy s{color:#777}
.product .buy a{margin-left:auto;font-size:11px;border:1px solid #ccc;padding:4px 9px}
.product .buy a.hot{background:var(--mint);border-color:var(--mint)}

/* exclusive offers */
.offers{top:1422px;left:0;width:1200px;height:446px;background:linear-gradient(90deg,#5e4a43,#7a6861 45%,#c9c1bd)}
.offers-portrait{left:640px;top:40px;width:420px;height:406px;background:radial-gradient(ellipse at 50% 40%,#d8d3d0,#8e8480 70%,transparent 72%)}
.offers h2{left:182px;top:88px;font-size:30px;color:#fff;font-weight:600;letter-spacing:.5px}
.offers ul{left:165px;top:145px;width:440px;list-style:none;color:#fff}
.offers li{font-size:18px;display:flex;gap:10px;align-items:center;margin-bottom:22px}
.offers p{font-size:13px;line-height:20px;color:#eee;margin:-12px 0 22px 29px}

/* brands */
.brands{top:1868px;left:0;width:1200px;height:208px;display:flex;justify-content:center;align-items:center;gap:70px;border-bottom:1px solid var(--line)}
.brands span{font-size:26px;color:#444;font-weight:400;letter-spacing:1px}
.brands .boxed{background:#d9d9d9;padding:20px 24px}

/* reviews */
.reviews{top:2108px;left:0;width:1200px;text-align:center}
.review{top:2172px;width:309px;text-align:center}
.review blockquote{background:var(--card);height:180px;padding:34px 24px;font-size:12px;line-height:21px;color:#555;text-align:justify}
.avatar{width:70px;height:70px;margin:-8px auto 0;background:linear-gradient(180deg,#c7b7a8,#8a7566)}
.review .name{color:var(--mint-deep);font-size:16px;margin-top:16px}
.review .role{color:var(--mint-deep);font-size:11px}
.stars{display:flex;justify-content:center;gap:5px;margin-top:8px}

/* rewards */
.rewards{top:2548px;left:0;width:1200px;height:185px;background:var(--mint)}
.rewards h2{left:165px;top:56px;font-size:19px;font-weight:400;color:var(--brown-dark)}
.rewards h2 b{font-weight:700}
.rewards p{left:165px;top:90px;width:320px;font-size:12px;line-height:18px;color:#3c4a43}
.signup{left:538px;top:70px;display:flex}
.signup .field{width:347px;height:40px;background:#fff;font-size:12px;color:#777;display:flex;align-items:center;justify-content:space-between;padding:0 18px}
.signup .submit{width:172px;height:40px;background:var(--brown);color:#fff;font-weight:700;font-size:15px;display:flex;align-items:center;justify-content:center}

/* footer */
.footer{top:2733px;left:0;width:1200px;height:298px}
.col{top:30px}
.col h4{font-size:17px;font-weight:400;margin-bottom:14px}
.col li{list-style:none;font-size:12px;margin-bottom:11px;display:flex;gap:8px;align-items:center}
.col li::before{content:"";width:6px;height:6px;border-radius:50%;background:#444}
.badge{background:#e8e8e8;border-radius:4px}
.footer .wordmark{font-size:30px}
.footer .wordmark i{width:12px;height:12px}
.about{left:832px;top:30px;width:260px}
.about h5{font-size:17px;font-weight:400;margin:6px 0 8px}
.about p{font-size:12px;line-height:20px;color:#444}
.pay{left:115px;top:258px;display:flex;gap:10px}
.pay span{width:42px;height:20px;border-radius:4px;background:#ddd}

/* bottom bar */
.bottombar{top:3031px;left:0;width:1200px;height:51px;background:var(--brown-dark);color:#fff;font-size:11px}
.bottombar .copy{left:110px;top:18px}
.social{right:110px;top:12px;display:flex;gap:14px}
.social span{width:27px;height:27px;border-radius:50%;background:#6b5953}
</style>
</head>
<body>

<div class="topbar abs">
  <span class="promo abs">Get your free promo code here</span>
  <nav class="account abs"><a>My Account</a><span class="sep">::</span><a>My Wishlist</a><span class="sep">::</span><a>My Cart</a><span class="sep">::</span><a>Checkout</a><span class="sep">::</span><a>Register</a><span class="sep">::</span><a>Log In</a></nav>
</div>

<header class="header abs">
  <div class="wordmark abs"><i></i>Pillbox Lounge</div>
  <div class="search abs"><span>Search Entire Store here...</span>
    <svg width="16" height="16" viewBox="0 0 16 16"><circle cx="6.5" cy="6.5" r="5" fill="none" stroke="#5cc194" stroke-width="2"/><line x1="10.5" y1="10.5" x2="15" y2="15" stroke="#5cc194" stroke-width="2"/></svg>
  </div>
</header>

<nav class="nav abs">
  <a class="current">Home</a><a>Brand</a><a>Supplements</a><a>Sports Nutrition</a><a>Haircare</a><a>Chiropractic Pillows</a><a>Health Condition</a><a>Beauty &amp; Skincare</a><a>Gluten Free</a><a>On Sale</a>
</nav>

<section class="hero abs">
  <div class="hero-photo abs" role="img" aria-label="Smiling woman taking a vitamin capsule"></div>
  <div class="wordmark abs"><i></i>Pillbox Lounge</div>
  <div class="hero-products abs" role="img" aria-label="Group of vitamin supplement bottles"></div>
  <div class="dots abs"><span></span><span></span><span></span><span></span></div>
</section>

<section class="usps abs">
  <div class="usp"><svg width="30" height="22" viewBox="0 0 30 22"><rect x="0" y="2" width="18" height="13" fill="#444"/><path d="M18 6h7l5 5v4H18z" fill="#444"/><circle cx="6" cy="18" r="3" fill="#444"/><circle cx="23" cy="18" r="3" fill="#444"/></svg><div><b>FREE Shipping</b><small>for all orders over $99!</small></div></div>
  <div class="usp"><svg width="22" height="26" viewBox="0 0 22 26"><path d="M11 1 21 5v8c0 6-4 10-10 12C5 23 1 19 1 13V5z" fill="none" stroke="#444" stroke-width="2.5"/></svg><div><b>Official Stockist</b><small>of more than 100 Brands</small></div></div>
  <div class="usp"><svg width="26" height="26" viewBox="0 0 26 26"><path d="M8 9V6a5 5 0 0 1 10 0v3" fill="none" stroke="#444" stroke-width="2.5"/><rect x="2" y="9" width="22" height="16" fill="#444"/></svg><div><b>2 FREE Samples</b><small>on all orders over $99!</small></div></div>
  <div class="usp"><svg width="26" height="26" viewBox="0 0 24 24"><path d="M12 1l3.4 7 7.6 1-5.5 5.3 1.3 7.6L12 18.3 5.2 21.9l1.3-7.6L1 9l7.6-1z" fill="#444"/></svg><div><b>Shopper Trusted Store</b><small>rating of 4.9/5</small></div></div>
</section>

<section class="welcome abs">
  <h2 class="section-title"><strong>Welcome To</strong> Pillbox Lounge</h2>
  <div class="rule"></div>
  <p>Lorem ipsum dolor sit amet, consectetur adipiscing elit, sed do eiusmod tempor incididunt ut labore et dolore magna aliqua. Ut enim ad minim veniam, quis nostrud exercitation ullamco laboris nisi ut aliquip ex ea commodo consequat.</p>
  <a class="btn-outline">Read more</a>
</section>

<div class="tabs abs"><span class="active">On Sale</span><span class="sep">|</span><span>New Arrivals</span><span class="sep">|</span><span>Recommended for you</span></div>

<article class="product abs" style="left:125px">
  <div class="thumb" role="img" aria-label="Amber supplement bottle"><div style="background:linear-gradient(90deg,#2b1a12,#7a3a1c,#2b1a12)"></div></div>
  <h3>3RD</h3>
  <div class="buy"><span>$22</span><s>$45</s><a class="hot">Add to Cart</a></div>
</article>
<article class="product abs" style="left:373px">
  <div class="thumb" role="img" aria-label="Verdana Health fibre supplement jar"><div style="background:linear-gradient(90deg,#ddd,#fff,#ddd)"></div></div>
  <h3>Restwell Pillow Standard Size Super Soft Density</h3>
  <div class="buy"><span>$22</span><s>$45</s><a>Add to Cart</a></div>
</article>
<article class="product abs" style="left:622px">
  <div class="thumb" role="img" aria-label="Black supplement tub"><div style="background:linear-gradient(90deg,#111,#333,#111);height:120px"></div></div>
  <h3>Restwell Pillow Standard Size Super Soft Density</h3>
  <div class="buy"><span>$22</span><s>$45</s><a>Add to Cart</a></div>
</article>
<article class="product abs" style="left:870px">
  <div class="thumb" role="img" aria-label="Three vitamin tablet jars"><div style="background:linear-gradient(90deg,#5a3a22,#b07a3c,#5a3a22);width:160px;height:140px"></div></div>
  <h3>Acne Control Tablets Extra Strength new</h3>
  <div class="buy"><span>$22</span><s>$45</s><a>Add to Cart</a></div>
</article>

<section class="offers abs">
  <div class="offers-portrait abs" role="img" aria-label="Woman surrounded by vitamin letter bubbles"></div>
  <h2 class="abs">EXCLUSIVE OFFERS</h2>
  <ul class="abs">
    <li><svg width="18" height="18" viewBox="0 0 18 18"><circle cx="9" cy="9" r="9" fill="#fff"/><path d="M5 9l3 3 5-6" fill="none" stroke="#6a5650" stroke-width="2"/></svg>Skin Care</li>
    <p>Lorem ipsum dolor sit amet, consectetur adipiscing elit, sed do eiusmod tempor incididunt ut labore et dolore magna aliqua. Ut enim ad minim veniam, quis nostrud exercitation ullamco laboris nisi ut aliquip ex ea commodo consequat.</p>
    <li><svg width="18" height="18" viewBox="0 0 18 18"><circle cx="9" cy="9" r="9" fill="#fff"/><path d="M5 9l3 3 5-6" fill="none" stroke="#6a5650" stroke-width="2"/></svg>Hair Care</li>
    <li><svg width="18" height="18" viewBox="0 0 18 18"><circle cx="9" cy="9" r="9" fill="#fff"/><path d="M5 9l3 3 5-6" fill="none" stroke="#6a5650" stroke-width="2"/></svg>Special Offers</li>
  </ul>
</section>

<section class="brands abs">
  <span>Aurelle</span><span>Maison Velour</span><span class="boxed">Clearvale</span><span>Solène</span>
</section>

<section class="reviews abs">
  <h2 class="section-title"><strong>Customer</strong> Reviews</h2>
</section>

<article class="review abs" style="left:103px">
  <blockquote>Morbi blandit venenatis semper. Nullam ut feugiat nibh. Quisque ac ultricies quam, quis aliquet orci. Phasellus eu nisi ultricies, porttitor augue nec, dictum velit. Proin rutrum fringilla cursus. Sed non odio magna.</blockquote>
  <div class="avatar" role="img" aria-label="Portrait of reviewer"></div>
  <div class="name">Clara Edmunds</div><div class="role">Lorium ipsum</div>
  <div class="stars"><svg width="90" height="14" viewBox="0 0 90 14" fill="#5cc194"><path id="st" d="M7 0l2 5h5l-4 3 1.5 5L7 10 2.5 13 4 8 0 5h5z"/><use href="#st" x="19"/><use href="#st" x="38"/><use href="#st" x="57"/><use href="#st" x="76"/></svg></div>
</article>
<article class="review abs" style="left:444px">
  <blockquote>Morbi blandit venenatis semper. Nullam ut feugiat nibh. Quisque ac ultricies quam, quis aliquet orci. Phasellus eu nisi ultricies, porttitor augue nec, dictum velit. Proin rutrum fringilla cursus. Sed non odio magna.</blockquote>
  <div class="avatar" role="img" aria-label="Portrait of reviewer"></div>
  <div class="name">Wilson</div><div class="role">Lorium ipsum</div>
  <div class="stars"><svg width="90" height="14" viewBox="0 0 90 14" fill="#5cc194"><use href="#st"/><use href="#st" x="19"/><use href="#st" x="38"/><use href="#st" x="57"/><use href="#st" x="76"/></svg></div>
</article>
<article class="review abs" style="left:790px">
  <blockquote>Morbi blandit venenatis semper. Nullam ut feugiat nibh. Quisque ac ultricies quam, quis aliquet orci. Phasellus eu nisi ultricies, porttitor augue nec, dictum velit. Proin rutrum fringilla cursus. Sed non odio magna.</blockquote>
  <div class="avatar" role="img" aria-label="Portrait of reviewer"></div>
  <div class="name">Rohan</div><div class="role">Lorium ipsum</div>
  <div class="stars"><svg width="90" height="14" viewBox="0 0 90 14" fill="#5cc194"><use href="#st"/><use href="#st" x="19"/><use href="#st" x="38"/><use href="#st" x="57"/><use href="#st" x="76"/></svg></div>
</article>

<section class="rewards abs">
  <h2 class="abs"><b>JOIN PILLBOX LOUNGE</b> REWARDS</h2>
  <p class="abs">Be rewarded with exclusive member offers, including discounts, sales, freebies, gifts-with purchase and competitions.</p>
  <div class="signup abs">
    <div class="field"><span>Enter Email Id</span><svg width="14" height="10" viewBox="0 0 14 10"><rect x=".5" y=".5" width="13" height="9" fill="none" stroke="#555"/><path d="M.5.5 7 6 13.5.5" fill="none" stroke="#555"/></svg></div>
    <div class="submit">Subscribe</div>
  </div>
</section>

<footer class="footer abs">
  <div class="col abs" style="left:110px"><h4>Useful Links</h4><ul><li>About Us</li><li>Customer Service</li><li>Privacy Policy</li></ul></div>
  <div class="col abs" style="left:325px"><h4>Products</h4><ul><li>About Us</li><li>Contact Us</li><li>Customer Service</li><li>Privacy Policy</li></ul></div>
  <div class="col abs" style="left:517px"><h4>Mobile App</h4>
    <div style="display:flex;gap:10px"><div class="badge" style="width:70px;height:36px"></div><div class="badge" style="width:75px;height:36px"></div></div>
    <div class="badge" style="width:130px;height:70px;margin:10px 0 0 58px"></div>
  </div>
  <div class="about abs">
    <div class="wordmark"><i></i>Pillbox Lounge</div>
    <h5>Welcome to Pillbox Lounge!</h5>
    <p>With savings of up to 70% off Recommended Retail Prices we invite you to choose to shop with us at Pillbox Lounge! Inside our online store you will find we are a leading Australian health retailer specialising in Professional. Fast and Reliable service for all your natural healthcare needs.</p>
  </div>
  <div class="pay abs"><span></span><span></span><span></span><span></span></div>
</footer>

<div class="bottombar abs">
  <span class="copy abs">© Copyright 2017.www.companyname.com</span>
  <div class="social abs"><span></span><span></span><span></span><span></span></div>
</div>

</body>
</html>
```